依頼詳細
シンプルというよりは、見やすくスッキリとしたデザインで目にとまるようなデザインにしたいです。

・角2封筒 表フルカラー
縦向き、郵便番号枠不要、住所記入線不要

・長3封筒 表フルカラー
横向き、郵便番号枠不要、住所記入線をお願いします。

インクモールへ印刷発注の為、専用テンプレートを使用し、そのままインクモールで印刷依頼が可能な仕様のデータで納品をお願いします。
デザインの印刷範囲制限がありますので、範囲内でお願いします。

封筒の色ですが、インクモールで封筒のサンプルを取り寄せ確認したところ、
クリニックのロゴが木のため、ペールノビア、ミルドトーンリーフがいいのではと考えております。
記載項目
記載項目などは添付ファイルをご参照ください。
希望イメージ
シンプル 複雑
単色 カラフル
暗い 明るい
日常 高級
遊び心 厳粛
未来的 伝統的
女性的 男性的
希望する色
納品ファイル
• 高解像度JPG (.jpg)
• イラストレーター形式 (.ai)
補足説明
添付したロゴを使用してください。
■ 選んだ理由

とてもきれいなデザインで気に入りました。

■ 提案者全員のお礼・コメント

素敵なデザインが多く迷いました。
たくさんのご提案ありがとうございます。

```html
<!DOCTYPE html>
<html lang="ja">
<head>
<meta charset="utf-8">
<title>あおば眼科 角2封筒</title>
<link rel="stylesheet" href="https://fonts.googleapis.com/css2?family=Noto+Sans+JP:wght@400;700&display=swap">
<style>
  :root {
    --page: #f4f4f4;
    --paper: #ffffff;
    --edge: #b9b9b9;
    --ink: #333333;
    --ink-soft: #666666;
    --leaf: #6fa85a;
    --leaf-faint: #eef3ea;
  }
  html, body {
    margin: 0;
    width: 853px;
    height: 1200px;
    overflow: hidden;
    background: var(--page);
    font-family: "Noto Sans JP", sans-serif;
  }
  .envelope {
    position: absolute;
    left: 114px;
    top: 78px;
    width: 631px;
    height: 1072px;
  }
  .envelope-shape { position: absolute; inset: 0; }
  .brand {
    position: absolute;
    left: 45px;
    top: 585px;
    display: flex;
    align-items: center;
    gap: 10px;
  }
  .brand-dot {
    width: 44px;
    height: 44px;
    border-radius: 50%;
    background: var(--leaf);
    flex: none;
  }
  .brand-text {
    color: var(--ink);
    font-weight: 700;
    line-height: 1.15;
  }
  .brand-area { font-size: 13px; display: block; }
  .brand-name { font-size: 30px; display: block; letter-spacing: 1px; }
  .brand-en { font-size: 10px; display: block; letter-spacing: 1.5px; }
  .contact {
    position: absolute;
    left: 45px;
    top: 690px;
    margin: 0;
    font-size: 10px;
    line-height: 1.8;
    color: var(--ink-soft);
  }
</style>
</head>
<body>
  <section class="envelope">
    <svg class="envelope-shape" width="631" height="1072" viewBox="0 0 631 1072">
      <path d="M1 70 L26 1 L605 1 L630 70 Z" fill="var(--paper)" stroke="var(--edge)" stroke-width="1.5"/>
      <rect x="1" y="70" width="629" height="1001" fill="var(--paper)" stroke="var(--edge)" stroke-width="1.5"/>
      <circle cx="476" cy="625" r="140" fill="var(--leaf-faint)" role="img" aria-label="淡いシンボル装飾"/>
    </svg>
    <div class="brand">
      <span class="brand-dot"></span>
      <span class="brand-text">
        <span class="brand-area">緑ヶ丘</span>
        <span class="brand-name">あおば眼科</span>
        <span class="brand-en">Aoba Eye Clinic</span>
      </span>
    </div>
    <p class="contact">
      〒123-4567 緑ヶ丘市若葉町1-2-3<br>
      TEL.00-0000-0000<br>
      https://www.aoba-eye.example
    </p>
  </section>
</body>
</html>
```